Bref créative
Business card and stationary design for home inspector
Keystone Ridge Home Inspection LLC
Professional
Walter Brunow
Owner/Founder
287 Fenwick Lane
Mooresville, NC 28942
walt@KeystoneRidgeHomeInspection.example
www.KeystoneRidgeHomeInspection.example
NC Home Inspector lic #6817
NC General Contractor lic # 58093
i would like to see both single and double sided business cards.... im not sure which i want yet... if you submit double sided maybe have my logo on the backside....

```html
<!DOCTYPE html>
<html lang="en">
<head>
<meta charset="utf-8">
<title>Keystone Ridge Home Inspection — Business Cards</title>
<link rel="stylesheet" href="https://fonts.googleapis.com/css2?family=Oswald:wght@600&family=Arimo:wght@400;700&display=swap">
<style>
  :root {
    --page-bg: #e9eaec;
    --brand-blue: #1f5f9e;
    --deep-blue: #174a80;
    --sky-blue: #6fa9dd;
    --mid-blue: #3a7cc0;
    --card-white: #ffffff;
    --text-grey: #5b6068;
    --rule-grey: #9aa3ad;
  }
  * { box-sizing: border-box; margin: 0; padding: 0; }
  html, body { width: 1200px; height: 901px; overflow: hidden; }
  body {
    background: var(--page-bg);
    font-family: "Arimo", Arial, sans-serif;
    position: relative;
  }
  .card {
    position: absolute;
    top: 296px;
    width: 540px;
    height: 309px;
    border-radius: 14px;
    overflow: hidden;
    box-shadow: 0 6px 18px rgba(0,0,0,0.18);
  }
  /* Back side */
  .card-back {
    left: 40px;
    background: linear-gradient(135deg, var(--sky-blue) 0%, var(--mid-blue) 55%, var(--deep-blue) 100%);
  }
  .card-back .backdrop-circle {
    position: absolute;
    left: 50px; top: 40px;
    width: 190px; height: 190px;
    border-radius: 50%;
    background: rgba(255,255,255,0.12);
  }
  .card-back .brand-name {
    position: absolute;
    right: 30px; bottom: 58px;
    text-align: right;
    color: var(--card-white);
    font-family: "Oswald", Impact, sans-serif;
    font-weight: 600;
    text-transform: uppercase;
    line-height: 1.05;
  }
  .card-back .brand-name .line-1 { font-size: 26px; display: block; }
  .card-back .brand-name .line-2 { font-size: 16px; letter-spacing: 1px; display: block; border-top: 1.5px solid rgba(255,255,255,0.8); padding-top: 2px; margin-top: 2px; }

  /* Front side */
  .card-front {
    left: 620px;
    background: var(--card-white);
  }
  .card-front .mark-circle {
    position: absolute;
    left: -40px; top: 40px;
    width: 230px; height: 230px;
    border-radius: 50%;
    background: radial-gradient(circle at 40% 35%, var(--mid-blue) 0%, var(--deep-blue) 100%);
  }
  .card-front .brand-name {
    position: absolute;
    right: 24px; top: 44px;
    text-align: right;
    color: var(--brand-blue);
    font-family: "Oswald", Impact, sans-serif;
    font-weight: 600;
    text-transform: uppercase;
    line-height: 1.05;
  }
  .card-front .brand-name .line-1 { font-size: 28px; display: block; }
  .card-front .brand-name .line-2 { font-size: 17px; letter-spacing: 1px; display: block; border-top: 1.5px solid var(--rule-grey); padding-top: 2px; margin-top: 3px; }

  .person {
    position: absolute;
    right: 24px; top: 138px;
    text-align: right;
  }
  .person .name { color: var(--brand-blue); font-weight: 700; font-size: 13px; }
  .person .title { color: var(--text-grey); font-size: 11px; margin-top: 2px; }

  .address {
    position: absolute;
    right: 24px; top: 176px;
    text-align: right;
    color: var(--text-grey);
    font-size: 10.5px;
    line-height: 1.4;
  }
  .licences {
    position: absolute;
    right: 24px; top: 210px;
    text-align: right;
    color: var(--text-grey);
    font-size: 9.5px;
    line-height: 1.4;
  }
  .contact {
    position: absolute;
    left: 206px; top: 246px;
    color: var(--text-grey);
    font-size: 10.5px;
    line-height: 1.5;
  }
  .contact .label { color: var(--brand-blue); font-weight: 700; margin-right: 3px; }
</style>
</head>
<body>
  <section class="card card-back" aria-label="Business card back">
    <div class="backdrop-circle"></div>
    <div class="brand-name">
      <span class="line-1">Keystone Ridge</span>
      <span class="line-2">Home Inspection</span>
    </div>
  </section>

  <section class="card card-front" aria-label="Business card front">
    <div class="mark-circle"></div>
    <div class="brand-name">
      <span class="line-1">Keystone Ridge</span>
      <span class="line-2">Home Inspection</span>
    </div>
    <div class="person">
      <p class="name">Walter Brunow</p>
      <p class="title">Owner/Founder</p>
    </div>
    <div class="address">
      <p>287 Fenwick Lane</p>
      <p>Mooresville, NC 28942</p>
    </div>
    <div class="licences">
      <p>NC Home Inspector lic #6817</p>
      <p>NC General Contractor lic # 58093</p>
    </div>
    <div class="contact">
      <p><span class="label">E:</span>walt@KeystoneRidgeHomeInspection.example</p>
      <p><span class="label">P:</span>704-555-0142</p>
      <p>www.KeystoneRidgeHomeInspection.example</p>
    </div>
  </section>
</body>
</html>
```